Health care technology software systems

We have a solid logo. We have company colors that will need to be used as well. We just need a great business card design. We sell to health plans but want to be modern
Updates

Need extra days to review

Target Market(s)

Health technology sector selling into Health Plans

Industry/Entity Type

Health Care Technology

Contact Information for Business Card

Name, title, address, phone number, email

Requirements
Must have
• Use of Kembrata corporate colors - Uploaded w/ our logos

```html
<!DOCTYPE html>
<html lang="en">
<head>
<meta charset="utf-8">
<title>Kembrata business card</title>
<link rel="stylesheet" href="https://fonts.googleapis.com/css2?family=Montserrat:wght@500;600;800&family=Lato:wght@300&display=swap">
<style>
  :root {
    --page: #cccccc;
    --card: #ffffff;
    --navy: #3b52a0;
    --sky: #2ca7e0;
    --leaf: #8cc43e;
    --ink: #3d3d3d;
    --text: #222222;
    --rule: #c8c8c8;
  }
  * { margin: 0; padding: 0; box-sizing: border-box; }
  html, body {
    width: 1200px; height: 1200px; overflow: hidden;
    background: var(--page);
  }
  .card {
    position: absolute; left: 246px; width: 707px; height: 403px;
    background: var(--card); overflow: hidden;
  }
  .card--front { top: 171px; }
  .card--back { top: 638px; }

  .accent { position: absolute; border-radius: 50%; }
  .front-navy { width: 300px; height: 300px; left: -150px; top: 150px; background: var(--navy); }
  .front-leaf { width: 220px; height: 220px; left: 440px; top: -150px; background: var(--leaf); }
  .front-sky  { width: 320px; height: 320px; left: 520px; top: 220px; background: var(--sky); }
  .back-pair  { width: 200px; height: 200px; left: 540px; top: -110px; background: var(--sky); }
  .back-leaf  { width: 230px; height: 230px; left: 30px; top: 280px; background: var(--leaf); }

  .texture {
    position: absolute; right: 0; bottom: 0; width: 270px; height: 130px;
    background: linear-gradient(135deg, rgba(240,240,240,0) 30%, rgba(232,232,232,0.8) 100%);
  }

  .brand {
    position: absolute; left: 0; right: 0;
    display: flex; align-items: center; justify-content: center; gap: 18px;
  }
  .card--front .brand { top: 160px; }
  .card--back .brand { top: 82px; }
  .brand-dot { width: 52px; height: 52px; border-radius: 50%; background: var(--sky); }
  .brand-name {
    font-family: "Lato", sans-serif; font-weight: 300;
    font-size: 58px; letter-spacing: 1px; color: var(--ink); line-height: 1;
  }

  .person {
    position: absolute; right: 363px; top: 206px; text-align: right;
    font-family: "Montserrat", sans-serif;
  }
  .person-name { font-weight: 800; font-size: 31px; color: var(--leaf); line-height: 1.1; }
  .person-title { font-weight: 600; font-size: 22px; color: var(--navy); letter-spacing: 1.5px; margin-top: 4px; }

  .divider { position: absolute; left: 369px; top: 209px; width: 2px; height: 62px; background: var(--rule); }

  .contact {
    position: absolute; left: 386px; top: 204px; list-style: none;
    font-family: "Montserrat", sans-serif; color: var(--text);
  }
  .contact li { display: flex; align-items: center; gap: 8px; }
  .contact svg { width: 14px; height: 14px; flex: none; }
  .contact-phone { font-weight: 600; font-size: 20px; }
  .contact-web { font-weight: 600; font-size: 20px; letter-spacing: 0.8px; margin-top: 2px; }
  .contact-address { font-weight: 500; font-size: 11px; letter-spacing: 0.8px; margin-top: 5px; }
</style>
</head>
<body>
  <section class="card card--front">
    <div class="accent front-leaf"></div>
    <div class="accent front-navy"></div>
    <div class="accent front-sky"></div>
    <div class="brand">
      <span class="brand-dot"></span>
      <span class="brand-name">kembrata</span>
    </div>
  </section>

  <section class="card card--back">
    <div class="accent back-pair"></div>
    <div class="accent back-leaf"></div>
    <div class="texture" role="img" aria-label="Faint geometric cube texture"></div>
    <div class="brand">
      <span class="brand-dot"></span>
      <span class="brand-name">kembrata</span>
    </div>
    <div class="person">
      <p class="person-name">LOREM NAME</p>
      <p class="person-title">CEO</p>
    </div>
    <div class="divider"></div>
    <ul class="contact">
      <li class="contact-phone">
        <svg viewBox="0 0 24 24" fill="none" stroke="#2ca7e0" stroke-width="2.5"><path d="M5 3h4l2 5-3 2a12 12 0 0 0 6 6l2-3 5 2v4a2 2 0 0 1-2 2A17 17 0 0 1 3 5a2 2 0 0 1 2-2z"/></svg>
        555-014-2290
      </li>
      <li class="contact-web">
        <svg viewBox="0 0 24 24" fill="none" stroke="#2ca7e0" stroke-width="2"><circle cx="12" cy="12" r="9"/><path d="M3 12h18M12 3c3 3 3 15 0 18M12 3c-3 3-3 15 0 18"/></svg>
        www.kembrata.com
      </li>
      <li class="contact-address">
        <svg viewBox="0 0 24 24" fill="#2ca7e0"><path d="M12 2a7 7 0 0 0-7 7c0 5 7 13 7 13s7-8 7-13a7 7 0 0 0-7-7zm0 9.5A2.5 2.5 0 1 1 12 6.5a2.5 2.5 0 0 1 0 5z"/></svg>
        Harbor City, Oregon 97000
      </li>
    </ul>
  </section>
</body>
</html>
```